Business Card Design needed for start up company Pramora

In need of a new business card designed for a start up company based in Sydney, Pramora is a new start up innovative Company, our mission it to make property accessible for everyday Australian and to become the leading Real Estate platform in Australia. We want it to be fresh and clean.

Industry/Entity Type

Financial

Contact Information for Business Card

Section for Name
Section for Title

PRAMORA - Where Doors Open Wide
Mobile:
Direct:

Font styles to use
Sans Serif

Colors
33a6d7
0692cd
0255a3
ffffff

Requirements
Must have
• Logo, all business card details

```html
<!DOCTYPE html>
<html lang="en">
<head>
<meta charset="utf-8">
<title>Pramora — Business Card</title>
<link rel="stylesheet" href="https://fonts.googleapis.com/css2?family=Jost:ital,wght@0,400;0,500;0,700;1,400&display=swap">
<style>
  :root {
    --backdrop: #e6e8eb;
    --card: #ffffff;
    --navy: #0255a3;
    --navy-deep: #14327a;
    --sky: #33a6d7;
    --blue: #0692cd;
    --ink: #4a4f57;
    --rule: #7d838c;
    --shadow: rgba(20, 30, 50, 0.18);
  }
  * { box-sizing: border-box; margin: 0; padding: 0; }
  html, body {
    width: 1200px; height: 848px; overflow: hidden;
    background: var(--backdrop);
    font-family: "Jost", "Helvetica Neue", Arial, sans-serif;
  }
  .sheet {
    width: 1200px; height: 848px;
    display: flex; align-items: center; justify-content: center; gap: 60px;
  }
  .card {
    position: relative;
    width: 520px; height: 297px;
    background: var(--card);
    border-radius: 4px;
    box-shadow: 0 14px 34px var(--shadow), 0 2px 6px var(--shadow);
  }

  /* brand name, set plainly in the text font */
  .brand-name {
    font-weight: 500; color: var(--navy);
    letter-spacing: 0.28em; line-height: 1;
  }

  /* front */
  .card-front { display: flex; flex-direction: column; align-items: center; justify-content: center; }
  .card-front .brand-name { font-size: 44px; padding-left: 0.28em; }
  .tagline {
    margin-top: 18px;
    font-size: 14px; font-style: italic; color: var(--navy-deep);
    letter-spacing: 0.04em;
  }

  /* back */
  .card-back .brand-name { position: absolute; top: 44px; right: 36px; font-size: 28px; letter-spacing: 0.24em; margin-right: -0.24em; }

  .person { position: absolute; top: 96px; left: 36px; }
  .person-name {
    font-size: 17px; font-weight: 700; color: var(--navy-deep);
    text-transform: uppercase; letter-spacing: 0.04em;
  }
  .person-title {
    font-size: 12px; color: var(--blue);
    text-transform: uppercase; letter-spacing: 0.06em; margin-top: 1px;
  }
  .contact-list { list-style: none; margin-top: 10px; }
  .contact-list li {
    display: flex; align-items: center; gap: 8px;
    font-size: 12px; color: var(--ink); line-height: 18px;
  }
  .contact-list svg { width: 11px; height: 11px; fill: var(--navy-deep); flex: none; }

  .divider {
    position: absolute; left: 36px; right: 36px; top: 210px;
    height: 1.5px; background: var(--rule);
  }
  .address {
    position: absolute; right: 36px; top: 220px;
    text-align: right; font-size: 12px; font-style: normal;
    color: var(--ink); line-height: 17px;
  }
</style>
</head>
<body>
<main class="sheet">

  <section class="card card-back" aria-label="Business card, contact side">
    <span class="brand-name">PRAMORA</span>

    <div class="person">
      <p class="person-name">Liam Carter</p>
      <p class="person-title">CEO / Founder</p>
      <ul class="contact-list">
        <li>
          <svg viewBox="0 0 24 24" aria-label="Mobile"><path d="M7 2h10a2 2 0 0 1 2 2v16a2 2 0 0 1-2 2H7a2 2 0 0 1-2-2V4a2 2 0 0 1 2-2zm0 3v13h10V5H7z"/></svg>
          612 480 3175
        </li>
        <li>
          <svg viewBox="0 0 24 24" aria-label="Direct"><path d="M6.6 10.8a15.5 15.5 0 0 0 6.6 6.6l2.2-2.2a1 1 0 0 1 1-.25 11.4 11.4 0 0 0 3.6.57 1 1 0 0 1 1 1V20a1 1 0 0 1-1 1A17 17 0 0 1 3 4a1 1 0 0 1 1-1h3.5a1 1 0 0 1 1 1c0 1.25.2 2.45.57 3.6a1 1 0 0 1-.25 1z"/></svg>
          612 480 3176
        </li>
        <li>
          <svg viewBox="0 0 24 24" aria-label="Email"><path d="M3 5h18a1 1 0 0 1 1 1v12a1 1 0 0 1-1 1H3a1 1 0 0 1-1-1V6a1 1 0 0 1 1-1zm9 7.2L4.5 7v1.9L12 14l7.5-5.1V7z"/></svg>
          liam@pramora.com.au
        </li>
      </ul>
    </div>

    <div class="divider"></div>

    <address class="address">
      42 Harbour Street<br>
      Sydney, NSW 2000<br>
      www.pramora.com.au
    </address>
  </section>

  <section class="card card-front" aria-label="Business card, brand side">
    <span class="brand-name">PRAMORA</span>
    <p class="tagline">Where Doors Open Wide</p>
  </section>

</main>
</body>
</html>
```